Poster for teenagers

Bright, trendy, modern and young fonts - a variety of fonts, plus arrows and clip art (no photos) for an A3 size poster to be hung in study halls of schools. There are six dot points. I think each point should be in some kind of box or circle.

Here are a few ideas of the kind of thing I mean.
http://www.tarnwick.example.au/Page/Images/youth_Advisory_Group_Poster_(1).jpg

http://www.holmbrae.example.ie/sites/default/files/Youth-Panel-Poster-1-Web.jpg

http://www.quillmarsh.example.au/images/librariesprovider4/Misc-illustrations/140335-qml-youth-superheros-heroup-highres.jpg?sfvrsn=0

https://rvkointernational.files.examplepress.com/2013/04/544477_432153653542694_970534114_n.jpg

Also my logo should be on it some where . I've attached a my logo.

Here is the text:
How to get organised and motivated this year.
1. Write stuff down
Write down things you need to do and when you plan to do them. Use digital calendars, to do apps and email lists – or pen and paper. Even if you are sure you will remember – get it out of your head and onto paper/your phone/laptop. You are more likely to get it done and feel less stressed.
2. Set up habits
If you do things in the same way, at the same time or after the same thing – then after a few weeks, it becomes much easier to get those things done. Set up a particular time, or place to do study tasks – or link them with another daily task. EG: art homework every Tuesday. Violin practice after breakfast.
3. Focus!
For 15-30 minutes at a time - totally focus on homework. Put your phone away, log out of chatterbox, close down other programs and really concentrate. Then have a break, send a text or whatever – and then go back to focussed study. Fifteen minutes of concentrated study gets more achieved than an hour of study switching back and forth between homework and other activities.
4. Just do something
No motivation? Just take a “bite”. Set a timer and just do 5 minutes. Or 15. Or read just the first two pages. Or the first problem on the worksheet. Something is better than nothing – and sometimes once you start, it’s easier to keep going.
5. Use rewards and consequences
Reward yourself when you do a hard task and use consequences when you don’t. Use food, fun activities, gaming and social time to motivate yourself – you get it when you do tasks, you don’t when you don’t. EG 15 minutes of vidloop when I finish this page. Tell other people your plans and you are more likely to stick to them.
6. Imagine the future
When you really can’t be find any motivation to do the things you need to do – take 30 seconds to think about what will happen in a week, month and year if you get on with it. What will happen then and how will that feel. And imagine what will happen in a week, month and year if you DON’T do those things – and how will that feel.

Good luck !
For free articles and one to one help with study skills, increasing motivation, coping with stress or tough times in senior school, go to brightpathlearning.example.au
Brightpath Learning Psychology and Education

```html
<!DOCTYPE html>
<html lang="en">
<head>
<meta charset="utf-8">
<title>How to get organised and motivated this year</title>
<link rel="stylesheet" href="https://fonts.googleapis.com/css2?family=Questrial&family=Kalam:wght@700&family=Arimo:wght@400&family=Courier+Prime&display=swap">
<style>
  :root {
    --paper: #ffffff;
    --title-fill: #a3a3a3;
    --title-edge: #2e2e2e;
    --green-deep: #12861b;
    --green-bright: #22c73a;
    --arrow-green: #5cc02a;
    --orange: #fb8c0c;
    --red: #d3181b;
    --dark-red: #8b1a1a;
    --purple: #9b1fb8;
    --blue: #3568d8;
    --blue-dot: #2d62e0;
    --cyan: #3ad6e0;
    --yellow: #f5ee1a;
    --grey-ring: #d9d9d9;
    --ink: #111111;
    --white: #ffffff;
  }
  html, body { margin: 0; padding: 0; overflow: hidden; background: var(--paper); }
  .poster {
    position: relative;
    width: 1000px;
    height: 1200px;
    overflow: hidden;
    background: var(--paper);
  }
  .shapes { position: absolute; inset: 0; z-index: 0; }
  .poster-title {
    position: absolute;
    left: 163px;
    top: 22px;
    margin: 0;
    z-index: 1;
    font-family: "Questrial", sans-serif;
    font-weight: 400;
    font-size: 50px;
    line-height: 56px;
    color: var(--title-fill);
    -webkit-text-stroke: 1.2px var(--title-edge);
    white-space: nowrap;
    letter-spacing: 0.5px;
  }
  .tip {
    position: absolute;
    margin: 0;
    z-index: 1;
    color: var(--white);
    white-space: nowrap;
  }
  .tip h2 { font: inherit; margin: 0; }
  .tip p { margin: 0; }
  .tip-write {
    left: 192px; top: 143px;
    font-family: "Kalam", cursive;
    font-weight: 700;
    font-size: 18.5px;
    line-height: 23.5px;
  }
  .tip-write h2 { padding-left: 30px; }
  .tip-habits {
    left: 535px; top: 230px; width: 390px;
    text-align: center;
    font-family: "Arimo", sans-serif;
    font-size: 19px;
    line-height: 25px;
  }
  .tip-focus {
    left: 138px; top: 496px; width: 350px;
    text-align: center;
    font-family: "Arimo", sans-serif;
    font-size: 19px;
    line-height: 22.6px;
  }
  .tip-rewards {
    left: 545px; top: 541px; width: 444px;
    text-align: center;
    font-family: "Courier Prime", monospace;
    font-size: 18px;
    line-height: 24.6px;
  }
  .tip-rewards h2 { font-size: 15px; }
  .tip-start {
    left: 300px; top: 868px; width: 320px;
    text-align: center;
    font-family: "Arimo", sans-serif;
    font-size: 19px;
    line-height: 25px;
  }
  .tip-future {
    left: 650px; top: 902px; width: 354px;
    text-align: center;
    font-family: "Arimo", sans-serif;
    font-size: 18.5px;
    line-height: 24.6px;
  }
  .sign-off {
    position: absolute;
    left: 160px; top: 1028px;
    margin: 0;
    font-family: "Arimo", sans-serif;
    font-size: 14.5px;
    line-height: 19.5px;
    color: var(--ink);
    white-space: nowrap;
    z-index: 2;
  }
</style>
</head>
<body>
<main class="poster">
  <svg class="shapes" width="1000" height="1200" viewBox="0 0 1000 1200" aria-hidden="true">
    <circle class="dot-red-top" cx="350" cy="50" r="42" fill="var(--red)"/>
    <circle class="ring-grey" cx="945" cy="525" r="62" fill="var(--grey-ring)"/>
    <path class="title-arrow" d="M640 44 H742 V134 H772 L706 196 L640 134 H716 V70 H640 Z"
          fill="var(--paper)" stroke="var(--arrow-green)" stroke-width="3" stroke-linejoin="round"/>
    <circle class="bubble-write" cx="345" cy="295" r="200" fill="var(--green-deep)"/>
    <circle class="dot-blue-top" cx="862" cy="220" r="43" fill="var(--blue-dot)"/>
    <circle class="bubble-habits" cx="730" cy="353" r="187" fill="var(--orange)"/>
    <circle class="dot-blue-mid" cx="540" cy="467" r="47" fill="var(--blue-dot)"/>
    <path class="arrow-zigzag" d="M478 500 L555 518 L590 496"
          fill="none" stroke="var(--cyan)" stroke-width="13" stroke-linejoin="round"/>
    <polygon class="arrow-zigzag-head" points="580,480 618,486 596,512" fill="var(--cyan)"/>
    <circle class="bubble-rewards" cx="767" cy="707" r="227" fill="var(--purple)"/>
    <path class="arrow-curve" d="M930 478 C985 520 980 565 952 598"
          fill="none" stroke="var(--yellow)" stroke-width="28" stroke-linecap="butt"/>
    <polygon class="arrow-curve-head" points="930,582 982,608 914,662" fill="var(--yellow)"/>
    <circle class="bubble-focus" cx="313" cy="640" r="180" fill="var(--red)"/>
    <path class="ribbon" d="M150 850 C190 820 215 870 255 845 C290 822 320 812 360 818"
          fill="none" stroke="var(--purple)" stroke-width="30"/>
    <path class="arrow-dark" d="M302 812 L380 866" stroke="var(--dark-red)" stroke-width="14"/>
    <circle class="dot-red-low" cx="960" cy="920" r="43" fill="var(--red)"/>
    <circle class="bubble-start" cx="460" cy="993" r="167" fill="var(--blue)"/>
    <circle class="bubble-future" cx="822" cy="1027" r="187" fill="var(--green-bright)"/>
  </svg>

  <h1 class="poster-title">How to get organised<br>and motivated this year</h1>

  <section class="tip tip-write">
    <h2>1.&nbsp;&nbsp;&nbsp;Write stuff down</h2>
    <p>Write down things you need to do<br>and when you plan to do them. Use<br>digital calendars, to do apps and<br>email lists – or pen and paper.<br>Even if you are sure you will<br>remember – get it out of your<br>head and onto paper/your<br>phone/laptop. You are more<br>likely to get it done and<br>feel less stressed.</p>
  </section>

  <section class="tip tip-habits">
    <h2>2.&nbsp;&nbsp;Set up habits</h2>
    <p>If you do things in the<br>same way, at the same time<br>or after the same thing – then after<br>a few weeks, it becomes much easier<br>to get those things done. Set up a<br>particular time, or place to do study<br>tasks – or link them with another daily<br>task. EG: art homework every Tuesday.<br>Violin practice after breakfast.</p>
  </section>

  <section class="tip tip-focus">
    <h2>3. Focus!</h2>
    <p>For 15-30 minutes at a time<br>- totally focus on homework. Put<br>your phone away, log out of chatterbox,<br>close down other programs and really<br>concentrate. Then have a break, send<br>a text or whatever – and then go<br>back to focussed study. Fifteen<br>minutes of concentrated study<br>gets more achieve than an hour<br>of study switching back and forth<br>between homework and other<br>activities.</p>
  </section>

  <section class="tip tip-rewards">
    <h2>5. Use rewards and consequences</h2>
    <p>Reward yourself when<br>you do a hard task and<br>use consequences when<br>you don’t. Use food,<br>fun activities, gaming and<br>social time to motivate yourself<br>- you get it when you do tasks, you<br>don’t when you don’t. EG 15 minutes<br>of vidloop when I finish this page.<br>Tell other people your plans and<br>you are more likely to<br>stick to them.</p>
  </section>

  <section class="tip tip-start">
    <h2>4.&nbsp;&nbsp;Just do something</h2>
    <p>No motivation? Just take a<br>“bite”. Set a timer and just do 5<br>minutes. Or 15. Or read just the<br>first two pages. Or the first<br>problem on the worksheet.<br>Something is better than nothing –<br>and sometimes once you start,<br>it’s easier to keep going.</p>
  </section>

  <section class="tip tip-future">
    <h2>6.&nbsp;&nbsp;Imagine the future</h2>
    <p>When you really can’t be find<br>any motivation to do the things<br>you need to do – take 30 seconds<br>to think about what will happen in a<br>week, month and year if you get<br>on with it. What will happen then and<br>how will that feel. And imagine what<br>will happen in a week, month and year<br>if you DON’T do those things –<br>and how will that feel.</p>
  </section>

  <p class="sign-off">Good luck !<br>For free articles and<br>one to one help with<br>study skills, increasing<br>motivation, coping with<br>stress or tough times in senior<br>&nbsp;school, go to<br>brightpathlearning.example.au Brightpath Learning Psychology and Education</p>
</main>
</body>
</html>
```